Prairie Pete''s Funhouse Website Revamp

We have a children's entertainment center that hasn't changed in 20 years and the site looks like it was created 20 years ago. We need a new, modern, clean site that pops. Attached is the new logo that should be used as a style guide.

Current site is: www.prairiepetesfun.example

Thanks!
Updates

Designers, thank you all for the amazing work. It was exciting to be able to go through and see all the creativity that came in. I have decided on a design but wanted to share my thanks and appreciation for your time. Warm regards, Colton

Target Market(s)

Mothers with children in the 2 - 14 range.

Industry/Entity Type

Entertainment

```html
<!DOCTYPE html>
<html lang="en">
<head>
<meta charset="utf-8">
<title>Prairie Pete's Funhouse</title>
<link href="https://fonts.googleapis.com/css2?family=Fredoka:wght@500;600&family=Open+Sans:wght@400;600;700&display=swap" rel="stylesheet">
<style>
:root{
  --teal:#1fb3c0;
  --teal-dark:#168c97;
  --green:#7cc242;
  --green-dark:#4f8f2c;
  --green-deep:#3b6f1f;
  --orange:#f5a524;
  --pink:#f28ea0;
  --ink:#555b61;
  --muted:#8a9096;
  --paper:#ffffff;
  --mist:#eeeeee;
}
*{box-sizing:border-box;margin:0;padding:0}
html,body{width:679px;height:1200px;overflow:hidden}
body{font-family:"Open Sans",sans-serif;color:var(--ink);background:var(--paper);position:relative}
.site-header{position:absolute;left:0;top:0;width:679px;height:90px;background:var(--paper);border-bottom:3px solid var(--teal)}
.brand{position:absolute;left:22px;top:22px;display:flex;align-items:center;gap:8px}
.brand-dot{width:14px;height:14px;border-radius:50%;background:var(--orange)}
.brand-name{font-family:"Fredoka",sans-serif;font-weight:600;font-size:19px;color:var(--teal);line-height:1.05;width:150px}
.social{position:absolute;right:18px;top:8px;display:flex;gap:5px}
.social span{width:13px;height:13px;border-radius:50%;background:var(--teal)}
.main-nav{position:absolute;right:20px;top:50px;display:flex;gap:30px;font-size:11px;color:var(--muted)}
.hero{position:absolute;left:0;top:93px;width:679px;height:360px;background:radial-gradient(circle at 30% 35%,#f7d89a 0,#c9853a 25%,#6b3a1c 60%,#2f1a10 100%)}
.hero-panel{position:absolute;left:396px;top:78px;width:232px;height:232px;border-radius:50%;background:rgba(124,194,66,.93)}
.hero-ribbon{position:absolute;left:338px;top:120px;width:300px;height:34px;background:var(--teal);clip-path:polygon(0 0,100% 0,96% 50%,100% 100%,0 100%,4% 50%);font-family:"Fredoka",sans-serif;font-weight:600;color:#fff;font-size:16px;letter-spacing:.5px;text-align:center;line-height:34px}
.hero-copy{position:absolute;left:428px;top:168px;width:170px;font-size:8.5px;line-height:1.45;color:#fff}
.hero-copy p+p{margin-top:8px}
.hero-dots{position:absolute;left:492px;top:286px;display:flex;gap:5px}
.hero-dots span{width:7px;height:7px;border-radius:50%;background:rgba(255,255,255,.55)}
.hero-dots span:first-child{background:#fff}
.attractions{position:absolute;left:0;top:453px;width:679px;height:270px;background:var(--mist);border-top:6px solid #e2e2e2}
.section-title{font-family:"Fredoka",sans-serif;font-weight:500;color:var(--green-dark);font-size:17px;text-align:center;padding-top:24px}
.cards{position:absolute;left:72px;top:80px;display:flex;gap:22px}
.card{width:164px;position:relative}
.card-label{position:relative;z-index:1;height:22px;margin:0 -10px;font-family:"Fredoka",sans-serif;font-size:11px;color:#fff;line-height:22px;padding-left:22px;clip-path:polygon(0 0,100% 0,96% 50%,100% 100%,0 100%,4% 50%)}
.card-photo{height:104px;margin-top:-4px;border:3px solid #fff}
.card.green .card-label{background:var(--green)}
.card.orange .card-label{background:var(--orange)}
.card.pink .card-label{background:var(--pink)}
.card.green .card-photo{background:linear-gradient(#b46a3c,#5d7c9a)}
.card.orange .card-photo{background:linear-gradient(#e8c27a,#8a4a2a)}
.card.pink .card-photo{background:linear-gradient(#d7b48a,#6b5238)}
.pager{position:absolute;left:322px;top:222px;display:flex;gap:8px}
.welcome{position:absolute;left:0;top:723px;width:679px;height:237px;background:var(--paper)}
.welcome-title{position:absolute;left:46px;top:46px;font-family:"Fredoka",sans-serif;font-weight:500;font-size:18px;color:var(--muted)}
.welcome-title em{font-style:normal;color:var(--green)}
.welcome-text{position:absolute;left:46px;top:88px;width:360px;font-size:9px;line-height:1.7;color:var(--muted)}
.welcome-art{position:absolute;left:458px;top:66px;width:196px;height:140px;border-radius:50%;background:radial-gradient(circle,#a8dff0 0,#dff4fb 70%,#fff 100%)}
.site-footer{position:absolute;left:0;top:960px;width:679px;height:240px;background:var(--green-dark)}
.footer-col{position:absolute;top:40px;font-size:9px;color:#fff}
.footer-col h3{font-family:"Open Sans",sans-serif;font-weight:600;font-size:10px;letter-spacing:1px;margin-bottom:12px}
.footer-col li{list-style:none;margin-bottom:5px;display:flex;align-items:center;gap:6px}
.footer-col li::before{content:"";width:4px;height:4px;border-radius:50%;background:#fff}
.contact li::before{display:none}
.contact svg{width:9px;height:9px;flex:none}
.quick-form input,.quick-form textarea{display:block;width:112px;height:18px;border:0;margin-bottom:6px;font:8px "Open Sans",sans-serif;padding:0 5px;color:var(--muted)}
.quick-form textarea{height:44px;padding-top:4px;resize:none}
.quick-form button{background:var(--teal);color:#fff;border:0;font:600 8px "Open Sans",sans-serif;padding:4px 12px}
.copyright{position:absolute;left:0;bottom:0;width:679px;height:34px;background:var(--green-deep);color:#d8e8cc;font-size:9px;line-height:34px;padding-left:46px}
</style>
</head>
<body>
<header class="site-header">
  <div class="brand"><span class="brand-dot"></span><span class="brand-name">Prairie Pete's Funhouse</span></div>
  <div class="social"><span></span><span></span><span></span></div>
  <nav class="main-nav"><span>Home</span><span>Attractions</span><span>Parties</span><span>Pricing</span><span>Directions</span><span>Contact</span></nav>
</header>

<section class="hero" role="img" aria-label="Photo of a smiling girl riding a lit carousel">
  <div class="hero-panel"></div>
  <div class="hero-ribbon">SAMPLE HEADING TEXT HERE</div>
  <div class="hero-copy">
    <p>Lorem ipsum dolor sit amet, consectetur adipiscing elit. Phasellus tincidunt tellus leo, sodales mattis quam et dolor.</p>
    <p>Lorem ipsum dolor sit amet, consectetur adipiscing elit. Phasellus tincidunt tellus leo, sodales mattis quam et dolor.</p>
  </div>
  <div class="hero-dots"><span></span><span></span><span></span></div>
</section>

<section class="attractions">
  <h2 class="section-title">Prairie Pete's Attractions</h2>
  <div class="cards">
    <div class="card green"><div class="card-label">Bumper Cars</div><div class="card-photo" role="img" aria-label="Photo of bumper cars in an arena"></div></div>
    <div class="card orange"><div class="card-label">Merry Go Round</div><div class="card-photo" role="img" aria-label="Photo of a merry-go-round"></div></div>
    <div class="card pink"><div class="card-label">Carousel</div><div class="card-photo" role="img" aria-label="Photo of carousel horses"></div></div>
  </div>
  <div class="pager">
    <svg width="12" height="14" viewBox="0 0 12 14"><path d="M11 1 2 7l9 6z" fill="#9aa0a5"/></svg>
    <svg width="12" height="14" viewBox="0 0 12 14"><path d="M1 1l9 6-9 6z" fill="var(--teal)"/></svg>
  </div>
</section>

<section class="welcome">
  <h2 class="welcome-title">Welcome to <em>The Funhouse!</em></h2>
  <p class="welcome-text">Prairie Pete's Funhouse is the Maple Valley's #1 indoor amusement park for young kids. We cater exclusively to children from infants to around 11 years old. Our climate controlled fun center offers a unique mix of seven different amusement park rides. Prairie Pete's also makes its own pizza with fresh ingredients that will satisfy any families appetite. Our family fun center is a fun, affordable and exciting birthday party place. Check out our birthday party packages or see your own birthday party ideas.</p>
  <div class="welcome-art" role="img" aria-label="Illustration of children riding a roller coaster"></div>
</section>

<footer class="site-footer">
  <div class="footer-col" style="left:57px">
    <h3>QUICKLINKS</h3>
    <ul><li>Home</li><li>Attractions</li><li>Parties</li><li>Pricing</li><li>Directions</li><li>Contact</li></ul>
  </div>
  <div class="footer-col" style="left:192px">
    <h3>USEFUL INFO</h3>
    <ul><li>FAQ</li><li>Sitemap</li><li>Terms &amp; Agreement</li><li>Privacy Policy</li></ul>
  </div>
  <div class="footer-col contact" style="left:328px">
    <h3>CONTACT INFO</h3>
    <ul>
      <li><svg viewBox="0 0 10 10"><path d="M5 0a3.5 3.5 0 0 0-3.5 3.5C1.5 6 5 10 5 10s3.5-4 3.5-6.5A3.5 3.5 0 0 0 5 0z" fill="#fff"/></svg>42 Sample Ave, Maple City,<br>MV 00000</li>
      <li><svg viewBox="0 0 10 10"><path d="M2 0h2l1 3-1.5 1a6 6 0 0 0 2.5 2.5L7 5l3 1v2a2 2 0 0 1-2 2A8 8 0 0 1 0 2a2 2 0 0 1 2-2z" fill="#fff"/></svg>111-111-1111</li>
      <li><svg viewBox="0 0 10 10"><rect x="0" y="2" width="10" height="7" fill="#fff"/><path d="M0 2l5 4 5-4" stroke="var(--green-dark)" fill="none"/></svg>info@prairiepetesfun.example</li>
    </ul>
  </div>
  <div class="footer-col" style="left:520px">
    <h3>QUICK MESSAGE</h3>
    <form class="quick-form">
      <input placeholder="Name">
      <input placeholder="Email">
      <textarea placeholder="Message"></textarea>
      <button type="button">Send Message</button>
    </form>
  </div>
  <div class="copyright">Copyright © 2014 Prairie Pete's All Rights Reserved</div>
</footer>
</body>
</html>
```